Brightwater Spectral Inquiry Website

We are a paranormal research group located in Central Mississippi. We are a group dedicated to help the community in any paranormal investigation. We use fresh new techniques with cutting edge technology to investigate any paranormal situation. Our services are always free of charge to anyone. An unique feature of our group is that we provide a complete history of the property, courtesy of our research team. We would like to see designs that incorporate our logo. We are a professional group and want a professional website.. we will need a home page that will reflect out goals. Links will include "Home, About Us, Contact us, (MAYBE MORE). We will also want a "blank page" with same links that we can edit and fill in all the information..

Target Market(s)

Paranormal-Ghost hunting groups

Industry/Entity Type

Community

Coding

Coded - Design and coding required

Number of Pages Required

2 page

Font styles to use
Other font styles liked:

Requirements
Must have
• we will need a home page that will reflect out goals. Links will include "Home, About Us, Contact us, (MAYBE MORE). We will also want a "blank page" with same links that we can edit and fill in all the information..

```html
<!DOCTYPE html>
<html lang="en">
<head>
<meta charset="utf-8">
<title>Brightwater Spectral Inquiry</title>
<link href="https://fonts.googleapis.com/css2?family=Creepster&family=Metal+Mania&family=Montserrat:wght@400;700&display=swap" rel="stylesheet">
<style>
  :root {
    --bg-deep: #0d0d0d;
    --bg-header: #1f1f1f;
    --bg-nav: #141414;
    --bg-wood: #1a1a1a;
    --bg-content: #1b1b1b;
    --nav-line: #333;
    --text-light: #e6e6e6;
    --text-body: #b9b9b9;
    --brand-gold: #e3cf3a;
    --brand-disc: #101010;
    --headline-red: #c81e12;
    --headline-orange: #f2a614;
    --field-bg: #121212;
    --field-border: #3a3a3a;
    --button-red: #a3140d;
    --hero-frame: #2a2c26;
  }
  * { box-sizing: border-box; margin: 0; padding: 0; }
  html, body { width: 1200px; height: 1001px; overflow: hidden; background: var(--bg-deep); }
  .page {
    position: relative; width: 1200px; height: 1001px; overflow: hidden;
    font-family: "Montserrat", sans-serif;
  }
  .site-header {
    position: absolute; left: 0; top: 0; width: 1200px; height: 146px;
    background: radial-gradient(ellipse at 50% 30%, #333 0%, var(--bg-header) 45%, #0f0f0f 100%);
  }
  .main-nav {
    position: absolute; left: 0; top: 146px; width: 1200px; height: 44px;
    background: linear-gradient(#262626, var(--bg-nav));
    border-top: 1px solid #3a3a3a; border-bottom: 1px solid #000;
  }
  .main-nav a {
    position: absolute; top: 0; height: 44px; line-height: 44px;
    font-family: "Metal Mania", cursive; font-size: 20px; color: var(--text-light);
    text-decoration: none; letter-spacing: 1px; transform: translateX(-50%);
    white-space: nowrap;
  }
  .nav-divider {
    position: absolute; top: 6px; width: 1px; height: 32px; background: var(--nav-line);
  }
  .brand {
    position: absolute; left: 513px; top: 34px; width: 174px; height: 174px;
    border-radius: 50%; background: var(--brand-disc);
    box-shadow: 0 0 0 3px #2a2a2a, 0 4px 14px #000;
    display: flex; align-items: center; justify-content: center;
  }
  .brand-name {
    width: 140px; text-align: center;
    font-family: "Montserrat", sans-serif; font-weight: 700; font-size: 17px;
    line-height: 22px; color: var(--brand-gold);
  }
  .wood-band {
    position: absolute; left: 0; top: 190px; width: 1200px; height: 464px;
    background: linear-gradient(90deg, #0a0a0a 0%, var(--bg-wood) 15%, #222 50%, var(--bg-wood) 85%, #0a0a0a 100%);
  }
  .hero {
    position: absolute; left: 172px; top: 252px; width: 860px; height: 358px;
    border: 6px solid var(--hero-frame); box-shadow: 0 0 18px #000, inset 0 0 10px #000;
    overflow: hidden;
  }
  .hero-photo {
    position: absolute; inset: 0;
    background:
      radial-gradient(ellipse 30% 35% at 57% 22%, rgba(230,225,215,0.85) 0%, rgba(230,225,215,0) 100%),
      radial-gradient(ellipse 22% 70% at 86% 70%, rgba(60,80,150,0.7) 0%, rgba(60,80,150,0) 100%),
      linear-gradient(100deg, #2a2420 0%, #3d3631 35%, #5a5550 52%, #26252a 70%, #101428 100%);
  }
  .hero-headline {
    position: absolute; left: 52px; top: 82px; transform: rotate(5deg); transform-origin: left top;
    font-weight: 400;
  }
  .hero-headline .line-main {
    display: block; font-family: "Creepster", cursive; font-size: 48px; line-height: 50px;
    color: var(--headline-red); letter-spacing: 2px;
  }
  .hero-headline .line-indent { padding-left: 196px; }
  .hero-headline .line-sub {
    display: block; font-family: "Metal Mania", cursive; font-size: 20px; line-height: 24px;
    color: var(--headline-orange); letter-spacing: 0.3px; white-space: nowrap;
  }
  .content {
    position: absolute; left: 0; top: 654px; width: 1200px; height: 288px; background: var(--bg-content);
  }
  .section-title {
    font-family: "Metal Mania", cursive; font-size: 29px; color: var(--text-light);
    letter-spacing: 1px; font-weight: 400; line-height: 34px;
  }
  .about { position: absolute; left: 162px; top: 22px; width: 654px; }
  .about .section-title { margin-bottom: 10px; }
  .about p { font-size: 11.4px; line-height: 17.4px; color: var(--text-body); margin-bottom: 17.4px; }
  .contact-form { position: absolute; left: 836px; top: 22px; width: 202px; }
  .contact-form .section-title { margin-bottom: 10px; white-space: nowrap; font-size: 26px; }
  .field {
    display: block; width: 202px; height: 27px; margin-bottom: 11.5px;
    background: var(--field-bg); border: 1px solid var(--field-border); border-radius: 3px;
    color: #8a8a8a; font-family: "Montserrat", sans-serif; font-size: 9.5px; padding-left: 8px; line-height: 25px;
  }
  .submit-button {
    display: flex; align-items: center; gap: 14px; margin-top: 3px;
    width: 97px; height: 29px; padding-left: 12px;
    background: linear-gradient(#c01a10, var(--button-red)); border: none; border-radius: 2px;
    font-family: "Metal Mania", cursive; font-size: 17px; color: #111; letter-spacing: 1px;
  }
  .site-footer {
    position: absolute; left: 0; top: 942px; width: 1200px; height: 59px;
    background: linear-gradient(#262626, #141414);
  }
  .site-footer small {
    position: absolute; left: 164px; top: 28px; font-family: "Metal Mania", cursive;
    font-size: 12px; color: #aaa; letter-spacing: 1px;
  }
</style>
</head>
<body>
<div class="page">
  <header class="site-header"></header>

  <div class="wood-band"></div>

  <nav class="main-nav">
    <a href="#" style="left:221px">HOME</a>
    <span class="nav-divider" style="left:274px"></span>
    <a href="#" style="left:338px">ABOUT US</a>
    <span class="nav-divider" style="left:405px"></span>
    <a href="#" style="left:462px">MENU 3</a>
    <a href="#" style="left:742px">MENU 4</a>
    <span class="nav-divider" style="left:798px"></span>
    <a href="#" style="left:855px">MENU 5</a>
    <span class="nav-divider" style="left:913px"></span>
    <a href="#" style="left:989px">CONTACT US</a>
  </nav>

  <div class="brand">
    <div class="brand-name">Brightwater Spectral Inquiry</div>
  </div>

  <section class="hero">
    <div class="hero-photo" role="img" aria-label="Old brick mansion at dusk with a woman looking up into blue light"></div>
    <h1 class="hero-headline">
      <span class="line-main">WE ARE A GROUP</span>
      <span class="line-main line-indent">DEDICATED</span>
      <span class="line-sub">TO HELP THE COMMUNITY PARANORMAL INVESTIGATION</span>
    </h1>
  </section>

  <main class="content">
    <article class="about">
      <h2 class="section-title">ABOUT BSI</h2>
      <p>Lorem ipsum dolor sit amet, consectetur adipiscing elit, sed do eiusmod tempor incididunt ut labore et dolore magna aliqua. Ut enim ad minim veniam, quis nostrud exercitation ullamco laboris nisi ut aliquip ex ea commodo consequat. Duis aute irure dolor in reprehenderit in voluptate velit esse cillum dolore eu fugiat nulla pariatur. Excepteur sint occaecat cupidatat non proident, sunt in culpa qui officia deserunt mollit anim id est labo</p>
      <p>Sed ut perspiciatis unde omnis iste natus error sit voluptatem accusantium doloremque laudantium, totam rem aperiam, eaque ipsa quae ab illo inventore veritatis et quasi architecto beatae vitae</p>
      <p>Neque porro quisquam est, qui dolorem ipsum quia dolor sit amet, consectetur, adipisci velit, sed quia non numquam eius modi tempora incidunt ut labore et dolore magnam aliquam quaerat voluptatem. Ut enim ad minima veniam, quis nostrum exercitationem ullam corporis.</p>
    </article>

    <form class="contact-form">
      <h2 class="section-title">FREE INVESTIGATION</h2>
      <span class="field">Your Name</span>
      <span class="field">Email</span>
      <span class="field">Phone no.</span>
      <span class="field">Tell us about case</span>
      <button type="button" class="submit-button">SUBMIT
        <svg width="9" height="12" viewBox="0 0 9 12" aria-hidden="true"><path d="M2 1l5 5-5 5" fill="none" stroke="#111" stroke-width="2.4"/></svg>
      </button>
    </form>
  </main>

  <footer class="site-footer">
    <small>COPYRIGHT © 2014. BSI. ALL RIGHTS RESERVED.</small>
  </footer>
</div>
</body>
</html>
```